Packaging label for launch of sun dried tomato products.

Established family farm in South Africa growing fruit for the production of dried fruit. We need a packaging label for the launch of our sun dried tomato products ie dried tomatoes in olive oil, dried tomato flakes and tomato powder. Packaging will be a round glass "jam jar" and spice shaker bottle. Due to limited amount of product available we cannot market to the masses, but rather focus on conveying a message of quality and exclusivity.

Target Market(s)

Home chef

Industry/Entity Type

Food

Font styles to use
Serif

Requirements
Nice to have
• Include the farm name in the design. KEVANTO

```html
<!DOCTYPE html>
<html lang="en">
<head>
<meta charset="utf-8">
<title>KEVANTO Sun Dried Tomatoes – Jar Label</title>
<link rel="stylesheet" href="https://fonts.googleapis.com/css2?family=Bebas+Neue&family=Open+Sans:wght@400&display=swap">
<style>
  :root {
    --backdrop: #efedea;
    --label-white: #ffffff;
    --ink: #111111;
    --tomato-red: #e3201f;
    --produce-light: #ea4a3a;
    --produce-deep: #c01a14;
  }
  html, body {
    margin: 0;
    padding: 0;
    width: 1200px;
    height: 900px;
    overflow: hidden;
    background: var(--backdrop);
  }
  .canvas {
    display: block;
    width: 1200px;
    height: 900px;
  }
  .label-sheet { fill: var(--label-white); }
  .frame-line { fill: none; stroke: var(--ink); stroke-width: 2; }
  .brand-name {
    font-family: "Open Sans", sans-serif;
    font-size: 76px;
    fill: var(--ink);
    letter-spacing: 1px;
  }
  .product-line {
    font-family: "Open Sans", sans-serif;
    font-size: 66px;
    fill: var(--ink);
  }
  .product-name {
    font-family: "Bebas Neue", sans-serif;
    font-size: 120px;
    fill: var(--tomato-red);
    letter-spacing: 2px;
  }
  .product-detail {
    font-family: "Open Sans", sans-serif;
    font-size: 29px;
    fill: var(--ink);
    letter-spacing: 4px;
  }
  .net-volume {
    font-family: "Open Sans", sans-serif;
    font-size: 18px;
    fill: var(--ink);
  }
</style>
</head>
<body>
<svg class="canvas" viewBox="0 0 1200 900" xmlns="http://www.w3.org/2000/svg">
  <defs>
    <linearGradient id="produce-tone" x1="0" y1="0" x2="0" y2="1">
      <stop offset="0%" stop-color="var(--produce-light)"/>
      <stop offset="100%" stop-color="var(--produce-deep)"/>
    </linearGradient>
    <clipPath id="label-shape">
      <path d="M240 210 Q600 20 960 210 L908 785 L292 785 Z"/>
    </clipPath>
    <path id="brand-arc" d="M360 292 Q600 205 845 292"/>
  </defs>

  <g class="jar-label">
    <path class="label-sheet" d="M240 210 Q600 20 960 210 L908 785 L292 785 Z"/>

    <g clip-path="url(#label-shape)">
      <rect class="produce-photo" role="img" aria-label="Photograph of fresh ripe red tomatoes on the vine"
            fill="url(#produce-tone)" x="230" y="585" width="740" height="210"/>
    </g>

    <path class="frame-line" d="M257 235 Q600 25 947 235 L890 760 L315 760 Z"/>
    <path class="frame-line" d="M352 212 Q600 110 852 220"/>
    <path class="frame-line" d="M385 298 Q600 228 810 298"/>

    <text class="brand-name" text-anchor="middle">
      <textPath href="#brand-arc" startOffset="50%">KEVANTO</textPath>
    </text>

    <text class="product-line" x="606" y="360" text-anchor="middle">Sun Dried</text>
    <text class="product-name" x="603" y="454" text-anchor="middle">TOMATOES</text>
    <line class="frame-line" x1="445" y1="466" x2="760" y2="464"/>
    <text class="product-detail" x="603" y="501" text-anchor="middle">in olive oil</text>
    <text class="net-volume" x="800" y="728">200ml</text>
  </g>
</svg>
</body>
</html>
```